Electrical needs letterhead design

Need a letterhead design for an electrical company. Using the same colours as to what are used in the logo.
After a modern design.

Want the logo in top right or top left.

Must include...

ABN 61 842 307 194
PHONE 0492357018
www.voltarnex.com.au
ben@voltarnex.com.au

'ABN' and 'PHONE' in bold.

Keep it basic. Logo top left, details either next to it or far right corner. Dont want any other objects included.

```html
<!DOCTYPE html>
<html lang="en">
<head>
<meta charset="utf-8">
<title>Voltarnex Letterhead</title>
<link href="https://fonts.googleapis.com/css2?family=Source+Sans+3:wght@400;700&family=Roboto+Condensed:wght@400;700&family=Pinyon+Script&display=swap" rel="stylesheet">
<style>
  :root {
    --brand-red: #9b2a23;
    --band-light: #d9482d;
    --band-dark: #8c1c19;
    --ink: #1a1a1a;
    --label-ink: #2a0b07;
    --paper: #ffffff;
  }
  * { margin: 0; padding: 0; box-sizing: border-box; }
  html, body { width: 848px; height: 1200px; overflow: hidden; background: var(--paper); }
  .letterhead {
    position: relative;
    width: 848px;
    height: 1200px;
    background: var(--paper);
    font-family: "Source Sans 3", "Myriad Pro", Arial, sans-serif;
    color: var(--ink);
  }
  .brand-name {
    position: absolute;
    left: 26px;
    top: 58px;
    font-size: 60px;
    font-weight: 400;
    line-height: 1;
    color: var(--brand-red);
    letter-spacing: -0.5px;
  }
  .salutation {
    position: absolute;
    left: 50px;
    top: 244px;
    font-size: 18px;
    font-weight: 700;
  }
  .letter-body {
    position: absolute;
    left: 50px;
    width: 740px;
    font-size: 15.6px;
    line-height: 20.5px;
    letter-spacing: -0.1px;
  }
  .letter-body p { position: absolute; left: 0; width: 740px; }
  .p1 { top: 287px; }
  .p2 { top: 395px; }
  .p3 { top: 486px; }
  .p4 { top: 620px; }
  .p5 { top: 671px; }
  .sign-off {
    position: absolute;
    left: 474px;
    top: 862px;
  }
  .sign-name {
    font-family: "Pinyon Script", "Great Vibes", cursive;
    font-size: 56px;
    line-height: 1;
    color: #111;
  }
  .sign-title {
    position: absolute;
    left: 148px;
    top: 68px;
    font-size: 22px;
    white-space: nowrap;
  }
  .contact-band {
    position: absolute;
    left: 0;
    bottom: 0;
    width: 848px;
    height: 46px;
    background: linear-gradient(90deg, var(--band-light) 0%, var(--band-light) 55%, var(--band-dark) 100%);
    font-family: "Roboto Condensed", "Arial Narrow", sans-serif;
    font-size: 14.5px;
    color: #fff;
  }
  .contact-item {
    position: absolute;
    top: 14px;
    white-space: nowrap;
  }
  .contact-item b { font-weight: 700; color: var(--label-ink); }
  .abn { left: 24px; }
  .phone { left: 179px; }
  .email { left: 339px; }
  .web { left: 576px; }
</style>
</head>
<body>
<main class="letterhead">
  <header>
    <div class="brand-name">Voltarnex</div>
  </header>

  <h1 class="salutation">Lorem ipsum dolor,</h1>

  <section class="letter-body">
    <p class="p1">Lorem ipsum dolor sit amet, consectetur adipisicing elit, sed do eiusmod tempor incididunt ut magna aliqua. Ut enim ad minim veniam, quis nostrud exercitation ullamco laboris nisi ut aliqu.</p>
    <p class="p2">Lorem ipsum dolor sit amet, consectetur adipisicing elit, sed do eiusmod tempor incididunt magna aliqua. Ut enim ad minim veniam, quis nostrud exercitation.</p>
    <p class="p3">Lorem ipsum dolor sit amet, consectetur adipisicing elit, sed do eiusmod tempor incididunt magna aliqua. Ut enim ad minim veniam, quis nostrud exercitation ullamco laboris nisi ut al do consequa.Lorem ipsum dolor sit amet, consectetur adipisicing elit, sed do eiusmod temp bore et dolore magna aliqua. Ut enim ad minim veniam, quis.</p>
    <p class="p4">Lorem ipsum dolor sit amet, consectetur adipisicing elit, sed do eiusmod tempor incididunt.</p>
    <p class="p5">Lorem ipsum dolor sit amet, consectetur adipisicing elit, sed do eiusmod tempor incididunt magna aliqua. Ut enim ad minim veniam, quis nostrud exercitation ullamco laboris nisi ut al do consequa.Lorem ipsum dolor sit amet, consectetur adipisicing elit, sed do eiusmod temp bore et dolore magna aliqua. Ut enim ad minim veniam, quis.</p>
  </section>

  <div class="sign-off">
    <div class="sign-name">Your Name</div>
    <div class="sign-title">Director</div>
  </div>

  <footer class="contact-band">
    <span class="contact-item abn"><b>ABN:</b> 61 842 307 194</span>
    <span class="contact-item phone"><b>PHONE:</b> 0492357018</span>
    <span class="contact-item email"><b>Email:</b> ben@voltarnex.com.au</span>
    <span class="contact-item web"><b>Web:</b> www.voltarnex.com.au</span>
  </footer>
</main>
</body>
</html>
```